New Toothpaste brand needs a logo & packaging design

Our company is launching a new toothpaste and is looking for a logo and packaging design. The toothpaste brand is called Brivana. The packaging should have the same design quality as the major international brands, such as Lumora, Lumora Totalcare, Dentiva, Pexolo, Wind-rise, Marvest, etc. The dominant colors for our brand should be hues of blue, similar to other major brands. In addition, there should be a little bit of green to represent the "Fresh Mint Blast" flavor and the "Extracts of Aloe Vera" included in the ingredients.

There are typically 3 unique sides on a toothpaste box:

The face: Repeated on ~3 sides of the 4 faces of the box
The back: The 4th box face has the instructions for use, ingredients, company information, bar code/product info, and some branding elements.
The sides: Usually consisting of just the logo, flavor etc.

Please refer to existing brands such as Lumora, Lumora Total-care, and Dentiva for an example of typical box layout and elements.

Task Details:
Package Dimensions: 180 mm x 48 mm x 28 mm, 100 ml toothpaste tube
Brand Name: Brivana
Description: Fluoride Toothpaste
Flavor: Fresh Mint Blast
5 Actions: Protects against cavities and tartar, freshens breath, whitens teeth, and maintains healthy gums. These actions can also be made into a list like Lumora Total Care or Dentiva Max care. For instance, Strong Teeth, Fresh Breath, Whitening, Healthy Gums, Cavity and Tartar Protection.
Also contains whitening micro particles and extracts of aloe vera which may be highlighted on the package

Overall, the look should be high quality and with the same look and feel as the big brands mentioned previously. We do not have an existing logo for this brand. The face of the package is the most important element as it is often repeated on several sides and on the tube itself.

Please let me know if you have any questions.

I've attached some of our favorite big brand designs below. I would say the Lumora Total Care and Gleam vers

The logos I've seen so far for Brivana, have been a bit too bold. A little bold is okay, but just needs to be moderate. 

I would like the colors to be bright and appealing. I mentioned shades of blue being the major color, but green should also be highlighted as well, perhaps in a 80% blue to 20% green ratio. 

Target Market(s)

adult consumer of toothpaste, both female and male.

Industry/Entity Type

It Company

Requirements
Must have
• A logo with the brand name: Brivana
Description or sub text: Fluoride Toothpaste
Flavor: Fresh Mint Blast
A phrase or list describing the Toothpaste Actions: e.g., Protects against cavities and tartar, freshens breath, whitens teeth, and maintains healthy gums. Or as a list simialr to Lumora Total Care or Dentiva Max Care:
-Anti-cavity
-Anti-tartar
-Fresh breath
-Whitening
-Healthy Gums

Special ingredient of "whitening micro particles: and "extracts of aloe vera", which should also be highlighted.

The color should mostly be shades of blue, with only a little bit of green to accentuate the fresh mint blast flavor and aloe vera

Nice to have
• The design should really look good next to lumora total care, gleam pure, and dentiva max care. These are our favorite designs.
Should not have
• For aloe vera, there is no need to show the plant.

The Brivana logo shouldn't be too Bold. This should be appeal to all consumers, not just men.

```html
<!DOCTYPE html>
<html lang="en">
<head>
<meta charset="utf-8">
<title>Brivana Fluoride Toothpaste – Carton Dieline</title>
<link href="https://fonts.googleapis.com/css2?family=Exo+2:ital,wght@0,700;1,700;1,800&display=swap" rel="stylesheet">
<style>
  :root {
    --paper: #ffffff;
    --rule: #1a1a1a;
    --band-cyan: #5eeefa;
    --band-light: #c4fafe;
    --mark-cyan: #45d4f3;
    --brand-blue: #1565c8;
    --deep-blue: #0d4fa8;
    --mint-green: #7fd61c;
    --leaf-green: #5cbf2e;
    --leaf-dark: #2d7a1b;
  }
  * { box-sizing: border-box; margin: 0; padding: 0; }
  html, body { width: 1200px; height: 779px; overflow: hidden; background: var(--paper); }
  body { position: relative; font-family: "Exo 2", Arial, sans-serif; }

  .panel { position: absolute; border: 1.5px solid var(--rule); background: var(--paper); overflow: hidden; }
  .top-flap   { left: 151px;  top: 12px;  width: 897px; height: 239px; }
  .face-upper { left: 151px;  top: 250px; width: 897px; height: 140px; }
  .face-main  { left: 151px;  top: 389px; width: 897px; height: 242px; }
  .face-lower { left: 151px;  top: 630px; width: 897px; height: 140px; }
  .side-left  { left: 11px;   top: 389px; width: 141px; height: 242px; }
  .side-right { left: 1047px; top: 389px; width: 142px; height: 242px; }

  .band {
    position: absolute; left: 23px; width: 874px;
    background:
      radial-gradient(ellipse 150px 70px at 110px 50%, #ffffff 0%, rgba(255,255,255,0) 100%),
      linear-gradient(90deg, var(--band-cyan) 0%, var(--band-cyan) 44%, var(--band-light) 57%, var(--band-cyan) 70%, var(--band-cyan) 100%);
  }
  .brand-square { position: absolute; background: var(--mark-cyan); }
  .brand-name {
    position: absolute; font-weight: 700; line-height: 1; letter-spacing: 1px;
    color: var(--brand-blue); white-space: nowrap;
  }
  .descriptor {
    position: absolute; font-style: italic; font-weight: 700;
    color: var(--brand-blue); white-space: nowrap;
  }
  .flavor {
    position: absolute; left: 444px;
    font-style: italic; font-weight: 800; font-size: 26px; line-height: 1;
    color: var(--mint-green);
    transform: rotate(-7deg); transform-origin: left top;
  }
  .flavor span { display: block; }
  .flavor span + span { margin-left: 6px; }
  .mint-leaves {
    position: absolute; left: 505px; width: 96px; height: 74px;
    border-radius: 50% 50% 45% 45%;
    background: radial-gradient(ellipse at 50% 40%, var(--leaf-green) 0%, var(--leaf-dark) 100%);
  }
  .benefits {
    position: absolute; left: 656px; list-style: none;
    font-style: italic; font-weight: 700; font-size: 12.5px; line-height: 16px;
    color: var(--deep-blue); white-space: nowrap;
  }
  .benefits li::before { content: "• "; }

  /* upper face */
  .face-upper .band         { top: 20px; height: 98px; }
  .face-upper .brand-square { left: 18px; top: 7px; width: 124px; height: 124px; }
  .face-upper .brand-name   { left: 156px; top: 32px; font-size: 46px; }
  .face-upper .descriptor   { left: 176px; top: 86px; font-size: 17px; }
  .face-upper .flavor       { top: 12px; }
  .face-upper .mint-leaves  { top: 52px; }
  .face-upper .benefits     { top: 34px; }

  /* main face */
  .face-main .band         { left: 18px; width: 879px; top: 49px; height: 121px; }
  .face-main .brand-square { left: 8px; top: 6px; width: 176px; height: 180px; }
  .face-main .brand-name   { left: 198px; top: 78px; font-size: 54px; }
  .face-main .descriptor   { left: 200px; top: 138px; font-size: 19px; }
  .face-main .flavor       { top: 80px; }
  .face-main .mint-leaves  { top: 104px; }
  .face-main .benefits     { top: 88px; }

  /* lower face */
  .face-lower .band         { top: 26px; height: 86px; }
  .face-lower .brand-square { left: 18px; top: 12px; width: 118px; height: 118px; }
  .face-lower .brand-name   { left: 154px; top: 34px; font-size: 46px; }
  .face-lower .descriptor   { left: 176px; top: 88px; font-size: 17px; }
  .face-lower .flavor       { top: 12px; }
  .face-lower .mint-leaves  { top: 54px; }
  .face-lower .benefits     { top: 40px; }

  /* side flaps */
  .side-name {
    position: absolute; left: 40px; top: 130px;
    transform: rotate(-90deg); transform-origin: left top;
    font-weight: 700; font-size: 28px; line-height: 1; letter-spacing: 1px;
    color: var(--brand-blue); white-space: nowrap;
  }
  .side-descriptor {
    position: absolute; left: 72px; top: 130px;
    transform: rotate(-90deg); transform-origin: left top;
    font-style: italic; font-weight: 700; font-size: 10px; line-height: 1;
    color: var(--brand-blue); white-space: nowrap;
  }
  .side-square {
    position: absolute; left: 34px; top: 138px; width: 70px; height: 86px;
    background: var(--mark-cyan);
  }
</style>
</head>
<body>

  <div class="panel top-flap"></div>

  <section class="panel face-upper">
    <div class="band"></div>
    <div class="brand-square"></div>
    <div class="brand-name">BRIVANA</div>
    <div class="descriptor">Fluoride Toothpaste</div>
    <div class="flavor"><span>Fresh Mint</span><span>Blast</span></div>
    <div class="mint-leaves" role="img" aria-label="Fresh mint leaves illustration"></div>
    <ul class="benefits">
      <li>Protect against cavity and tartar</li>
      <li>Freshens breath</li>
      <li>Whitens teeth</li>
      <li>Maintains healthy gums</li>
    </ul>
  </section>

  <section class="panel side-left">
    <div class="side-name">BRIVANA</div>
    <div class="side-descriptor">Fluoride Toothpaste</div>
    <div class="side-square"></div>
  </section>

  <section class="panel face-main">
    <div class="band"></div>
    <div class="brand-square"></div>
    <div class="brand-name">BRIVANA</div>
    <div class="descriptor">Fluoride Toothpaste</div>
    <div class="flavor"><span>Fresh Mint</span><span>Blast</span></div>
    <div class="mint-leaves" role="img" aria-label="Fresh mint leaves illustration"></div>
    <ul class="benefits">
      <li>Protect against cavity and tartar</li>
      <li>Freshens breath</li>
      <li>Whitens teeth</li>
      <li>Maintains healthy gums</li>
    </ul>
  </section>

  <section class="panel side-right">
    <div class="side-name">BRIVANA</div>
    <div class="side-descriptor">Fluoride Toothpaste</div>
    <div class="side-square"></div>
  </section>

  <section class="panel face-lower">
    <div class="band"></div>
    <div class="brand-square"></div>
    <div class="brand-name">BRIVANA</div>
    <div class="descriptor">Fluoride Toothpaste</div>
    <div class="flavor"><span>Fresh Mint</span><span>Blast</span></div>
    <div class="mint-leaves" role="img" aria-label="Fresh mint leaves illustration"></div>
    <ul class="benefits">
      <li>Protect against cavity and tartar</li>
      <li>Freshens breath</li>
      <li>Whitens teeth</li>
      <li>Maintains healthy gums</li>
    </ul>
  </section>

</body>
</html>
```